Visually Compelling Flyer Design - Orvane Benefits

We are a life insurance company looking to create visually compelling flyers that gain attention of potential buyers and simplify the concept. It should be professional, friendly, approachable in nature. Our logo and several rough drafts are included.
We are looking to refine this look and make it ultra professional, clean and easy to follow. A creative brief with brand guidelines is also included.
FLYER 1 — PAY YOURSELF FIRST
EYEBROW TAG
YOUR COMPANY JUST UPGRADED YOUR BENEFITS
HEADLINE
One small decision. A lifetime of protection.
SUBHEADLINE
Permanent life insurance + long-term care coverage, starting at $1 a day.
EYEBROW TAG
CHOOSE YOUR DAILY INVESTMENT
STAT — TIER 1
$1 / day → $20,000 Life Insurance
STAT — TIER 2 (HERO — make this one biggest/most prominent)
$2 / day → $40,000 Life Insurance
★ Most Popular
STAT — TIER 3
$3 / day → $60,000 Life Insurance
CAPTION
Rate locked at enrollment. Benefit never decreases.
EYEBROW TAG
THREE BENEFITS. ONE POLICY.
SUBHEADLINE
Your money works three ways.
CALLOUT — BENEFIT 1
01 | Cash Value Growth
BODY
Averages 6% annually over the last 50 years — guaranteed never to fall below 3%. Better than any savings account. And if you ever need it, you can borrow against it. It's your money.
CALLOUT — BENEFIT 2
02 | Tax-Free Death Benefit
BODY
From day one, your family is protected. The full benefit is paid tax-free to the person you choose — no waiting period, no exceptions. That's your legacy, preserved.
CALLOUT — BENEFIT 3
03 | Long-Term Care Coverage
BODY
70% of Americans will need long-term care. This plan pays 75% of your benefit — upfront and tax-free — to cover those costs while you're still alive. Your retirement savings stay intact. Your family stays protected.
EYEBROW TAG
ALREADY HAVE LIFE INSURANCE THROUGH WORK?
SUBHEADLINE
That's term. It ends when you need it most.
BODY
Term life insurance is designed for temporary needs — protecting your paycheck, your mortgage, your kids while they're home. When you retire, the house is paid off and your children are grown. Term ends because the need ends.
BODY
But one need never ends: your final expenses and the cost of long-term care. This permanent plan stays with you after retirement — when term coverage is gone and getting new coverage is expensive or impossible.
COMPARISON — LEFT COLUMN HEADER
✕ TERM LIFE
COMPARISON — LEFT COLUMN ITEMS
Gets more expensive with age
Ends at retirement
No cash value
Temporary protection only
COMPARISON — RIGHT COLUMN HEADER
✓ THIS PLAN
COMPARISON — RIGHT COLUMN ITEMS
Rate locked forever at enrollment
Stays with you after retirement
Builds real cash value
Permanent protection for life
EYEBROW TAG
WHAT MAKES THIS DIFFERENT
SUBHEADLINE
Built for you. Stays with you.
CALLOUT
✓ Guaranteed Issued
No medical exams. No questions asked. You qualify.
CALLOUT
✓ Group Rate
Because you work here, you get pricing individuals can't access on their own.
CALLOUT
✓ Rate Locked Forever
Your premium never increases. Your benefit never decreases.
CALLOUT
✓ Portable
Change jobs. Retire. Your policy comes with you at the same rate.
CALLOUT
✓ Family Coverage
Protect your spouse and children under the same plan.
SUBHEADLINE
Protect retirement. Preserve dignity. Plan ahead.
CTA
Be on the lookout for your personalized coverage details.
CAPTION
Brokered by Orvane Benefits · Underwritten by TrelloraLife
FLYER 2 — THE LONG-TERM CARE REALITY
EYEBROW TAG
WHAT MOST PEOPLE DON'T KNOW — BUT SHOULD
HEADLINE
Most Americans are unprepared. You don't have to be.
SUBHEADLINE
The long-term care gap is real — and it affects families like yours.
EYEBROW TAG
THE NUMBERS ARE HARD TO IGNORE
STAT
70%
of Americans age 65 and older will need some form of long-term care during their lifetime.
CAPTION
Source: Pike & Marsden, Review of Elder Welfare and Civic Planning, 2018
STAT
3–4%
of Americans over 50 own a private long-term care insurance policy. The gap between who needs it and who has it is staggering.
CAPTION
Source: Dunn & Solberg, QRT Wellness Wire, 2023
STAT
$700 Billion+
Estimated annual U.S. long-term care cost — and it's growing every year.
CAPTION
Source: Brandt Lowe & Petrasek, Civic Policy Roundtable, 2020
STAT
$470 Billion
The estimated value of unpaid care provided by family members every year. That's the real cost — measured in time, stress, and financial sacrifice.
CAPTION
Source: Lindqvist & Oram, Harborline Institute
STAT
80%
of total long-term care spending goes directly to assist retirees. This isn't a young person's problem. But the time to plan is now.
CAPTION
SUBHEADLINE
Long-term care doesn't just cost money. It costs families.
BODY
When there's no plan in place, the people you love absorb the impact — financially, emotionally, and physically. Retirement savings built over a lifetime can disappear in months. Family members step back from their own lives to provide care. Dignity becomes a daily negotiation.
BODY
This is not inevitable. A small decision today changes the entire outcome.
EYEBROW TAG
THE SOLUTION
HEADLINE
The Pay Yourself First Principle.
BODY
Take the first $1, $2, or $3 you make every day and invest it in a permanent life insurance policy that includes long-term care coverage — underwritten by TrelloraLife, offered through your employer at a group rate, and Guaranteed Issued for everyone.
STAT
$1 / day → $20,000 $2 / day → $40,000 $3 / day → $60,000
BODY
The benefit includes three protections in one: a cash value that grows at an average of 6% annually, a tax-free death benefit for your family, and long-term care coverage that pays 75% of your benefit upfront — tax-free — when you need care most.
SUBHEADLINE
Whether you're single, married, with children or without — there is protection in this plan for you.
HEADLINE
CTA
Look for your personalized offer. Coverage details are coming your way.
CAPTION
COPY RULES FOR DESIGNERS
Headlines are one idea only. Never more than two lines.
Stats stand alone. Never buried in a paragraph.
Body copy maxes at 3 sentences per block. If it's longer, cut it.
The $2/day tier is always the hero. Always.
"Guaranteed Issued" appears on both flyers. It's the most important trust signal.
TrelloraLife is always attributed. Always.
The tagline is: Protect retirement. Preserve dignity. Plan ahead. — Use it verbatim.
Target Market(s)
Average Americans with a family - adults looking for life insurance
Industry/Entity Type
Life Insurance & Financial Retirement

```html
<!DOCTYPE html>
<html lang="en">
<head>
<meta charset="utf-8">
<title>Orvane Benefits — Pay Yourself First</title>
<link href="https://fonts.googleapis.com/css2?family=Montserrat:wght@500;600;700;800&family=Inter:wght@400;500;600&display=swap" rel="stylesheet">
<style>
  :root{
    --navy-deep:#070b3a;
    --navy:#0c1466;
    --royal:#1636c9;
    --blue:#1f5be8;
    --sky:#2bb3f2;
    --cyan:#39d7ff;
    --green:#22c22f;
    --green-dark:#1f9e28;
    --ink:#111827;
    --ink-soft:#2b3245;
    --ice:#eaf5fd;
    --white:#ffffff;
  }
  *{box-sizing:border-box;margin:0;padding:0}
  html,body{width:683px;height:1200px;overflow:hidden;background:var(--white)}
  body{font-family:"Inter",Arial,sans-serif;color:var(--ink)}
  .flyer{position:relative;width:683px;height:1200px;overflow:hidden;background:var(--white)}
  .abs{position:absolute}

  /* hero band */
  .hero{position:absolute;left:0;top:0;width:683px;height:578px;
    background:
      radial-gradient(ellipse 260px 200px at 340px 470px, rgba(43,179,242,.55), transparent 70%),
      radial-gradient(ellipse 380px 260px at 520px 120px, rgba(30,70,200,.45), transparent 70%),
      linear-gradient(180deg,#08104a 0%,#0b1a78 55%,#1740c8 100%);}
  .hero-rays{position:absolute;left:0;top:330px;width:683px;height:248px;
    background:repeating-linear-gradient(90deg,rgba(80,170,255,.10) 0 6px,transparent 6px 22px);
    -webkit-mask:linear-gradient(180deg,transparent,#000 70%);mask:linear-gradient(180deg,transparent,#000 70%)}
  .brand{position:absolute;left:15px;top:0;width:104px;height:116px;background:#05060f;border-radius:0 0 10px 10px;
    display:flex;flex-direction:column;align-items:center;justify-content:center;gap:8px}
  .brand-dot{width:26px;height:26px;border-radius:50%;background:var(--sky)}
  .brand-name{font-family:"Montserrat",sans-serif;font-weight:600;font-size:11px;color:var(--white);text-align:center;line-height:1.2}
  .kicker{left:0;width:683px;top:29px;text-align:center;font-family:"Montserrat",sans-serif;font-weight:700;font-size:12.5px;color:var(--cyan)}
  .kicker span{border-bottom:1px solid var(--cyan);padding-bottom:3px}
  .kicker b{color:var(--green);font-size:12px;margin-right:4px}
  .pill-tag{position:absolute;display:flex;align-items:center;justify-content:center;border-radius:30px;
    font-family:"Montserrat",sans-serif;font-weight:700;letter-spacing:.1px}
  .upgrade{left:166px;top:68px;width:351px;height:35px;background:#1a2580;color:var(--white);font-size:11.3px}
  .upgrade em{font-style:normal;color:var(--cyan);margin-left:4px}
  .headline{left:0;width:683px;top:110px;text-align:center;font-family:"Montserrat",sans-serif;font-weight:800;
    font-size:36px;line-height:42px;color:var(--white);letter-spacing:-.3px}
  .subhead{left:0;width:683px;top:206px;text-align:center;font-size:12.5px;color:var(--white);font-weight:500}
  .subhead em{font-style:normal;color:var(--cyan);font-weight:700}
  .plane-area{left:540px;top:124px;width:90px;height:120px;border-radius:45px;
    background:radial-gradient(ellipse at 50% 40%,rgba(60,170,240,.28),rgba(60,170,240,0) 70%)}
  .choose{left:224px;top:253px;width:237px;height:32px;background:linear-gradient(90deg,#1e3ed6,#2aa9f0);color:var(--white);font-size:11.3px}

  .tier{position:absolute;border-radius:12px;text-align:center}
  .tier-badge{position:absolute;left:50%;width:38px;height:38px;margin-left:-19px;border-radius:50%;display:flex;align-items:center;justify-content:center}
  .tier-price{font-family:"Montserrat",sans-serif;font-weight:800;line-height:1}
  .tier-price small{font-size:15px;font-weight:600;margin-left:4px}
  .tier-arrow{font-size:16px;line-height:1;margin:6px 0 4px}
  .tier-amount{font-family:"Montserrat",sans-serif;font-weight:800;line-height:1}
  .tier-label{font-size:13px;font-weight:500;margin-top:4px}
  .tier-1{left:41px;top:282px;width:174px;height:159px;background:var(--white);color:var(--ink);padding-top:28px}
  .tier-1 .tier-badge{top:-16px;background:#1b2a8c}
  .tier-1 .tier-price{font-size:31px;color:var(--green-dark)}
  .tier-1 .tier-price small{color:var(--ink)}
  .tier-1 .tier-amount{font-size:28px;color:var(--royal)}
  .tier-2{left:236px;top:316px;width:209px;height:218px;color:var(--white);padding-top:42px;
    background:linear-gradient(180deg,#2bb6f4 0%,#1d6fe4 55%,#1430b8 100%)}
  .tier-2 .tier-badge{top:-16px;background:var(--green)}
  .tier-2 .tier-price{font-size:32px}
  .tier-2 .tier-arrow{color:#bfe8ff}
  .tier-2 .tier-amount{font-size:30px;color:var(--cyan)}
  .popular{display:inline-block;margin-top:26px;width:128px;height:21px;line-height:21px;border-radius:12px;background:var(--sky);
    font-weight:600;font-size:12px;color:var(--white)}
  .tier-3{left:468px;top:285px;width:174px;height:206px;color:var(--white);padding-top:34px;
    border:2px solid #3aa0ff;background:linear-gradient(180deg,#283cb0 0%,#2350d6 70%,#3b7ff0 100%)}
  .tier-3 .tier-badge{top:-16px;background:var(--white)}
  .tier-3 .tier-price{font-size:30px}
  .tier-3 .tier-amount{font-size:29px;color:var(--cyan)}

  .spot{left:0;top:520px;width:683px;height:60px}
  .locked{left:0;width:683px;top:545px;text-align:center;font-size:13px;line-height:16.5px;color:var(--ink);font-weight:500}

  /* benefits band */
  .burst{left:-40px;top:600px;width:190px;height:260px;border-radius:50%;
    background:radial-gradient(circle,rgba(43,179,242,.35),rgba(43,179,242,0) 70%)}
  .three{position:absolute;left:118px;top:594px;width:443px;height:33px;border:1px solid var(--ink);border-radius:20px;display:flex;overflow:hidden;background:var(--white)}
  .three-tag{width:235px;background:linear-gradient(90deg,#15219a,#2a8ff0);color:var(--white);font-family:"Montserrat",sans-serif;font-weight:700;font-size:11.3px;
    display:flex;align-items:center;justify-content:center;border-radius:20px}
  .three-sub{flex:1;display:flex;align-items:center;padding-left:14px;font-size:12px;font-weight:500}
  .benefits{position:absolute;left:24px;top:644px;width:633px;height:197px;background:var(--ice);border-radius:12px;
    display:flex;padding:18px 10px 0 18px;box-shadow:0 2px 8px rgba(20,40,120,.12)}
  .benefit{flex:1;padding:0 10px}
  .benefit + .benefit{border-left:1px solid #b8c4d6}
  .benefit-head{display:flex;align-items:center;gap:8px;height:32px;margin-bottom:10px}
  .benefit-title{flex:1;font-family:"Montserrat",sans-serif;font-weight:700;font-size:11.8px;line-height:14px;color:var(--royal)}
  .benefit-num{width:22px;height:22px;border-radius:50%;background:var(--royal);color:var(--white);font-family:"Montserrat",sans-serif;font-weight:600;font-size:12px;
    display:flex;align-items:center;justify-content:center}
  .benefit-body{font-size:10.6px;line-height:16.7px;color:var(--ink-soft)}

  /* comparison band */
  .compare{position:absolute;left:0;top:852px;width:683px;height:270px;
    background:linear-gradient(90deg,#0a1a86 0%,#1535c0 50%,#1c3ec8 100%)}
  .term-copy{left:27px;top:882px;width:196px;color:var(--white)}
  .term-copy h3{font-family:"Montserrat",sans-serif;font-weight:800;font-size:10.8px;line-height:13.5px;letter-spacing:-.2px}
  .term-copy .lead{color:var(--cyan);font-size:8.6px;line-height:11px;font-weight:600;margin:6px 0 11px}
  .term-copy p{font-size:8.6px;line-height:10.9px;text-align:justify;margin-bottom:8px}
  .col{position:absolute;border-radius:10px;overflow:hidden}
  .col-head{height:26px;display:flex;align-items:center;justify-content:center;font-family:"Montserrat",sans-serif;font-weight:800;font-size:12.5px;color:var(--white)}
  .col ul{list-style:none;padding:0 10px 0 5px}
  .col li{display:flex;align-items:center;gap:6px;font-size:7.9px;font-weight:600;line-height:10px;min-height:27px}
  .term{left:231px;top:890px;width:122px;height:179px;background:var(--white)}
  .term .col-head{background:#111522}
  .term li{color:var(--ink);border-bottom:1px solid #ccd2dc}
  .term li:last-child{border-bottom:0}
  .plan{left:360px;top:880px;width:122px;height:179px;border:1.5px solid #2f86f5;background:linear-gradient(180deg,#1d57e8,#1437c3)}
  .plan .col-head{background:#1c64ec}
  .plan li{color:#e8f0ff;border-bottom:1px solid rgba(255,255,255,.25)}
  .plan li:last-child{border-bottom:0}
  .diff{left:505px;top:870px;width:170px;color:var(--white)}
  .diff h3{font-family:"Montserrat",sans-serif;font-weight:800;font-size:11.6px;line-height:13.5px}
  .diff .lead{color:var(--cyan);font-size:8.6px;font-weight:600;margin:3px 0 8px}
  .perk{display:flex;gap:8px;margin-bottom:6px}
  .perk-tick{flex:none;width:16px;height:16px;border-radius:50%;background:var(--green);display:flex;align-items:center;justify-content:center;margin-top:2px}
  .perk b{display:block;font-weight:500;font-size:10.2px;line-height:13px}
  .perk span{display:block;font-size:7.2px;line-height:9px;color:#dbe4ff}

  /* footer */
  .footer{position:absolute;left:0;top:1120px;width:683px;height:60px;background:var(--navy-deep);border-top:2px solid var(--white)}
  .seal{left:27px;top:1098px;width:84px;height:84px;border-radius:50%;background:var(--white);display:flex;align-items:center;justify-content:center}
  .seal-inner{width:70px;height:70px;border-radius:50%;background:linear-gradient(180deg,#2a8ff0,#1533c0);display:flex;align-items:center;justify-content:center}
  .tagline{left:120px;width:440px;top:1124px;text-align:center;font-family:"Montserrat",sans-serif;font-weight:700;font-size:15.5px;color:var(--white)}
  .cta{position:absolute;left:137px;top:1151px;width:401px;height:25px;border-radius:8px;background:var(--green);color:var(--navy-deep);
    font-family:"Montserrat",sans-serif;font-weight:700;font-size:12px;display:flex;align-items:center;justify-content:center}
  .credit{position:absolute;left:0;top:1180px;width:683px;height:20px;background:#eef1f6;text-align:center;font-size:7.5px;line-height:20px;color:var(--ink)}
</style>
</head>
<body>
<main class="flyer">
  <section class="hero">
    <div class="hero-rays"></div>
  </section>

  <div class="brand">
    <div class="brand-dot"></div>
    <div class="brand-name">Orvane<br>Benefits</div>
  </div>

  <p class="abs kicker"><b>★</b><span>Pay Yourself First</span></p>
  <div class="pill-tag upgrade">YOUR COMPANY JUST UPGRADED YOUR <em>BENEFITS</em></div>
  <div class="abs plane-area" role="img" aria-label="Paper plane illustration with dotted flight path"></div>
  <h1 class="abs headline">One small decision.<br>A lifetime of protection.</h1>
  <p class="abs subhead">Permanent life insurance + long-term care coverage, starting at <em>$1</em> a day.</p>

  <div class="pill-tag choose">CHOOSE YOUR DAILY INVESTMENT</div>

  <svg class="abs spot" viewBox="0 0 683 60" aria-hidden="true"><polygon points="236,14 445,14 520,58 162,58" fill="#ffffff"/></svg>

  <article class="tier tier-1">
    <div class="tier-badge"><svg width="16" height="16" viewBox="0 0 16 16"><path d="M3.5 8.5l3 3 6-7" fill="none" stroke="#fff" stroke-width="2" stroke-linecap="round" stroke-linejoin="round"/></svg></div>
    <div class="tier-price">$1<small>/ day</small></div>
    <div class="tier-arrow">→</div>
    <div class="tier-amount">$20,000</div>
    <div class="tier-label">Life Insurance</div>
  </article>

  <article class="tier tier-3">
    <div class="tier-badge"><svg width="16" height="16" viewBox="0 0 16 16"><path d="M3.5 8.5l3 3 6-7" fill="none" stroke="#1f5be8" stroke-width="2" stroke-linecap="round" stroke-linejoin="round"/></svg></div>
    <div class="tier-price">$3<small>/ day</small></div>
    <div class="tier-arrow">→</div>
    <div class="tier-amount">$60,000</div>
    <div class="tier-label">Life Insurance</div>
  </article>

  <article class="tier tier-2">
    <div class="tier-badge"><svg width="16" height="16" viewBox="0 0 16 16"><path d="M3.5 8.5l3 3 6-7" fill="none" stroke="#fff" stroke-width="2" stroke-linecap="round" stroke-linejoin="round"/></svg></div>
    <div class="tier-price">$2<small>/ day</small></div>
    <div class="tier-arrow">→</div>
    <div class="tier-amount">$40,000</div>
    <div class="tier-label">Life Insurance</div>
    <div class="popular">Most Popular</div>
  </article>

  <p class="abs locked">Rate locked at enrollment.<br>Benefit never decreases.</p>

  <div class="abs burst" role="img" aria-label="Soft blue radiating burst decoration"></div>

  <div class="three">
    <div class="three-tag">THREE BENEFITS. ONE POLICY.</div>
    <div class="three-sub">Your money works three ways.</div>
  </div>

  <section class="benefits">
    <div class="benefit">
      <div class="benefit-head">
        <svg width="30" height="30" viewBox="0 0 30 30" aria-hidden="true"><g fill="none" stroke="#1f5be8" stroke-width="1.5"><rect x="3" y="20" width="4" height="8"/><rect x="10" y="15" width="4" height="13"/><rect x="17" y="10" width="4" height="18"/><rect x="24" y="5" width="4" height="23"/><path d="M3 15l8-7 5 3 10-9"/></g></svg>
        <div class="benefit-title">Cash Value<br>Growth</div>
        <div class="benefit-num">1</div>
      </div>
      <p class="benefit-body">Averages 6% annually over the last 50 years — guaranteed never to fall below 3%. Better than any savings account. And if you ever need it, you can borrow against it. It's your money.</p>
    </div>
    <div class="benefit">
      <div class="benefit-head">
        <svg width="30" height="30" viewBox="0 0 30 30" aria-hidden="true"><g fill="none" stroke="#1f5be8" stroke-width="1.5"><circle cx="15" cy="8" r="5"/><path d="M3 14v7l6 6h4v-5l-4-5M27 14v7l-6 6h-4v-5l4-5"/></g></svg>
        <div class="benefit-title">Tax-Free Death<br>Benefit</div>
        <div class="benefit-num">2</div>
      </div>
      <p class="benefit-body">From day one, your family is protected. The full benefit is paid tax-free to the person you choose no waiting period, no exceptions. That's your legacy, preserved.</p>
    </div>
    <div class="benefit">
      <div class="benefit-head">
        <svg width="30" height="30" viewBox="0 0 30 30" aria-hidden="true"><g fill="none" stroke="#1f5be8" stroke-width="1.5"><rect x="3" y="5" width="19" height="21" rx="2"/><path d="M3 10h19M7 3v4M18 3v4M7 15h8M7 19h6"/><circle cx="23" cy="22" r="5"/><path d="M23 19.5v3l2 1"/></g></svg>
        <div class="benefit-title">Long-Term<br>Care Coverage</div>
        <div class="benefit-num">3</div>
      </div>
      <p class="benefit-body">70% of Americans will need long-term care. This plan pays 75% of your benefit — upfront and tax free — to cover those costs while you're still alive. Your retirement savings stay intact. Your family stays protected.</p>
    </div>
  </section>

  <section class="compare"></section>

  <div class="abs term-copy">
    <h3>ALREADY HAVE LIFE INSURANCE<br>THROUGH WORK?</h3>
    <p class="lead">That's term. It ends when you<br>need it most.</p>
    <p>Term life insurance is designed for temporary needs — protecting your paycheck, your mortgage, your kids while they're home. When you retire, the house is paid off and your children are grown. Term ends because the need ends.</p>
    <p>But one need never ends: your final expenses and the cost of long-term care. This permanent plan stays with you after retirement — when term coverage is gone and getting new coverage is expensive or impossible.</p>
  </div>

  <div class="col term">
    <div class="col-head">TERM LIFE</div>
    <ul>
      <li><svg width="8" height="8" viewBox="0 0 8 8"><path d="M1 1l6 6M7 1L1 7" stroke="#111" stroke-width="1.2"/></svg>Gets more expensive with age</li>
      <li><svg width="8" height="8" viewBox="0 0 8 8"><path d="M1 1l6 6M7 1L1 7" stroke="#111" stroke-width="1.2"/></svg>Ends at retirement</li>
      <li><svg width="8" height="8" viewBox="0 0 8 8"><path d="M1 1l6 6M7 1L1 7" stroke="#111" stroke-width="1.2"/></svg>No cash value</li>
      <li><svg width="8" height="8" viewBox="0 0 8 8"><path d="M1 1l6 6M7 1L1 7" stroke="#111" stroke-width="1.2"/></svg>Temporary protection only</li>
    </ul>
  </div>

  <div class="col plan">
    <div class="col-head">THIS PLAN</div>
    <ul>
      <li><svg width="11" height="11" viewBox="0 0 12 12"><circle cx="6" cy="6" r="5" fill="none" stroke="#cfe0ff"/><path d="M3.5 6l2 2 3-4" fill="none" stroke="#cfe0ff"/></svg>Rate locked forever at enrollment</li>
      <li><svg width="11" height="11" viewBox="0 0 12 12"><circle cx="6" cy="6" r="5" fill="none" stroke="#cfe0ff"/><path d="M3.5 6l2 2 3-4" fill="none" stroke="#cfe0ff"/></svg>Stays with you after retirement</li>
      <li><svg width="11" height="11" viewBox="0 0 12 12"><circle cx="6" cy="6" r="5" fill="none" stroke="#cfe0ff"/><path d="M3.5 6l2 2 3-4" fill="none" stroke="#cfe0ff"/></svg>Builds real cash value</li>
      <li><svg width="11" height="11" viewBox="0 0 12 12"><circle cx="6" cy="6" r="5" fill="none" stroke="#cfe0ff"/><path d="M3.5 6l2 2 3-4" fill="none" stroke="#cfe0ff"/></svg>Permanent protection for life</li>
    </ul>
  </div>

  <div class="abs diff">
    <h3>WHAT MAKES THIS<br>DIFFERENT</h3>
    <p class="lead">Built for you. Stays with you.</p>
    <div class="perk"><div class="perk-tick"><svg width="9" height="9" viewBox="0 0 10 10"><path d="M2 5l2 2 4-4.5" fill="none" stroke="#fff" stroke-width="1.6"/></svg></div><div><b>Guaranteed Issued</b><span>No medical exams. No questions asked. You qualify.</span></div></div>
    <div class="perk"><div class="perk-tick"><svg width="9" height="9" viewBox="0 0 10 10"><path d="M2 5l2 2 4-4.5" fill="none" stroke="#fff" stroke-width="1.6"/></svg></div><div><b>Group Rate</b><span>Because you work here, you get pricing individuals can't access on their own.</span></div></div>
    <div class="perk"><div class="perk-tick"><svg width="9" height="9" viewBox="0 0 10 10"><path d="M2 5l2 2 4-4.5" fill="none" stroke="#fff" stroke-width="1.6"/></svg></div><div><b>Rate Locked Forever</b><span>Your premium never increases. Your benefit never decreases.</span></div></div>
    <div class="perk"><div class="perk-tick"><svg width="9" height="9" viewBox="0 0 10 10"><path d="M2 5l2 2 4-4.5" fill="none" stroke="#fff" stroke-width="1.6"/></svg></div><div><b>Portable</b><span>Change jobs. Retire. Your policy comes with you at the same rate.</span></div></div>
    <div class="perk"><div class="perk-tick"><svg width="9" height="9" viewBox="0 0 10 10"><path d="M2 5l2 2 4-4.5" fill="none" stroke="#fff" stroke-width="1.6"/></svg></div><div><b>Family Coverage</b><span>Protect your spouse and children under the same plan.</span></div></div>
  </div>

  <footer class="footer"></footer>
  <div class="abs seal"><div class="seal-inner"><svg width="34" height="34" viewBox="0 0 34 34"><path d="M8 17l6 6 12-13" fill="none" stroke="#fff" stroke-width="4" stroke-linecap="round" stroke-linejoin="round"/></svg></div></div>
  <p class="abs tagline">Protect retirement. Preserve dignity. Plan ahead.</p>
  <div class="cta">Be on the lookout for your personalized coverage details.</div>
  <p class="credit">Brokered by Orvane Benefits · Underwritten by TrelloraLife</p>
</main>
</body>
</html>
```